Brightwell Cleaning Services - Redesign

I've got my website designed a few years ago and it looks dated now. I would like to get a modern, happy, bright, and clean look. All the content needed can be found at my current website www.brightwellhq.example. Not necessarily need to use all of it, since I want something more clean and easy to read.
I need a 5 pages website:
HOME | SERVICES | ESTIMATE |TESTIMONIALS | CONTACT US

Industry/Entity Type

Janitorial Service

Number of Pages Required

5+ page

Colors
0792cd
34a6d7
85cae6
cee9f5
ebebeb
f0f0f0
f5f5f5
b1b1b1
000000

Requirements
Must have
• Who we are?
• Brightwell Cleaning Services is a local, family-owned, client-focused house and office cleaning company that strives to ensure the highest level of customer satisfaction. We offer expert residential and commercial cleaning services to all the Seattle and Eastside areas.
• Why Brightwell?
• √ We are insured, bonded and licensed.
•  Brightwell Cleaning Service is Fully Insured so you can rest easy knowing your home is protected.
•  Copy of insurance available upon request.
•

√ We provide all supplies and equipments needed to thoroughly clean your home or business.

• √ We are not a franchise. We are a local, family-owned company.

• When you call Brightwell Cleaning Services, you’ll always speak to one of the owners, which is a great benefit to you since this allows us to give you the personal attention and more time needed to clean your home the way you want it cleaned.

• √ We are good at what we do, and we like doing it.

```html
<!DOCTYPE html>
<html lang="en">
<head>
<meta charset="utf-8">
<title>Brightwell Cleaning Services</title>
<link href="https://fonts.googleapis.com/css2?family=Lato:ital,wght@0,400;0,700;0,900;1,400&display=swap" rel="stylesheet">
<style>
:root{
  --blue:#0792cd;
  --blue-mid:#34a6d7;
  --blue-soft:#85cae6;
  --blue-pale:#cee9f5;
  --grey-1:#ebebeb;
  --grey-2:#f0f0f0;
  --grey-line:#b1b1b1;
  --dark:#222222;
  --ink:#1a1a1a;
  --text:#333333;
}
*{box-sizing:border-box;margin:0;padding:0}
a{text-decoration:none}
html,body{width:777px;height:1200px;overflow:hidden;background:#fff}
body{position:relative;font-family:'Lato',sans-serif;color:var(--text)}
.abs{position:absolute}

.topbar{left:0;top:0;width:777px;height:38px;background:var(--dark);color:#fff;font-size:10.5px}
.topbar .contact{position:absolute;top:11px;display:flex;align-items:center;gap:6px}
.topbar .email{left:437px}
.topbar .phone{left:627px;font-weight:700;font-size:11px}

.brand{left:64px;top:44px;display:flex;align-items:center;gap:8px}
.brand .dot{width:14px;height:14px;border-radius:50%;background:var(--blue)}
.brand .name{font-size:17px;font-weight:900;color:var(--blue);line-height:1.1;width:160px}

.nav{left:296px;top:53px;display:flex;font-size:9.5px;font-weight:700;color:var(--ink);letter-spacing:.2px}
.nav a{color:inherit;height:23px;line-height:23px;padding:0 6px;margin-right:1px}
.nav a.active{background:var(--blue-mid);color:#fff;padding:0 8px;margin-right:3px}

.hero{left:0;top:100px;width:777px;height:340px;overflow:hidden}
.hero .ph{position:absolute;inset:0;background:linear-gradient(90deg,#bcd9ee 0%,#dde9f2 18%,#b9c3cc 32%,#9aa4b0 48%,#c9ced4 60%,#e6eef4 72%,#e9c758 82%,#c8e1f2 92%,#b7d5ec 100%)}
.hero .arrow{position:absolute;top:158px;width:26px;height:26px;border-radius:50%;background:#eee;border:2px solid #bbb;display:flex;align-items:center;justify-content:center}
.hero .caption{position:absolute;left:0;bottom:0;width:100%;height:37px;background:rgba(40,40,40,.82);color:#fff;font-size:18.5px;font-weight:900;text-align:center;line-height:37px;letter-spacing:.3px}

.welcome{left:65px;top:468px;width:410px}
.welcome h1{font-size:21px;font-weight:700;color:var(--ink);padding-bottom:10px;border-bottom:1px solid #ccc}
.welcome h1 span,.blue{color:var(--blue)}
.welcome .lead{margin-top:9px;font-size:11.5px;font-weight:700;color:var(--ink)}
.welcome p.body{margin-top:7px;font-size:10px;line-height:20px;color:#444}
.btn{display:inline-block;background:var(--blue);color:#fff;font-size:10.5px;font-weight:700;height:22px;line-height:22px;padding:0 9px}
.welcome .btn{margin-top:13px}

.inquiry{left:491px;top:481px;width:222px;height:176px;border:1px solid #d5d5d5;background:#fff}
.inquiry .tab{position:absolute;left:35px;top:-9px;width:150px;height:27px;background:var(--blue);color:#fff;font-size:12px;font-weight:700;text-align:center;line-height:27px;letter-spacing:.3px}
.inquiry .field{position:absolute;left:15px;width:196px;height:21px;border:1px solid #ccc;font-size:8.5px;color:#333;padding:6px 5px}
.inquiry .field i{color:#d22;font-style:normal}
.inquiry .btn{position:absolute;left:16px;top:147px;width:72px;text-align:center;font-size:10px}

.section-title{left:0;width:777px;text-align:center;font-size:21px;font-weight:700;color:var(--ink)}
.divider{left:0;width:777px;height:14px}

.services-lead{left:0;top:743px;width:777px;text-align:center;font-size:12.3px;color:#333}
.card{top:774px;width:197px;height:136px}
.card .ph{height:108px}
.card .label{height:28px;background:var(--blue-mid);color:#fff;font-size:14.5px;font-weight:900;line-height:28px;padding-left:8px;letter-spacing:.2px}

.testimonial{left:70px;top:1012px;width:640px;height:100px}
.avatar{position:absolute;left:0;top:0;width:100px;height:100px;border-radius:50%;border:2px solid #e6e6e6;background:radial-gradient(circle at 45% 45%,#f1d6c2 0%,#b9d2e6 55%,#8fb3cf 100%)}
.quote{position:absolute;left:77px;top:26px;width:46px;height:46px;border-radius:50%;background:var(--blue);color:#fff;font-size:38px;font-weight:900;text-align:center;line-height:56px}
.testimonial .words{position:absolute;left:141px;top:18px;width:485px;font-size:8.6px;line-height:16px;color:#333}
.testimonial .who{position:absolute;left:141px;top:71px;font-size:11px;font-style:italic;color:var(--blue)}
.side-arrow{top:1051px}

.footer{left:0;top:1144px;width:777px;height:56px;background:var(--grey-1);border-top:2px solid var(--blue-mid)}
.footer .links{position:absolute;left:65px;top:20px;font-size:9px;color:#333}
.footer .links span{margin:0 8px;color:#555}
.footer .copy{position:absolute;right:64px;top:12px;text-align:right;font-size:9px;line-height:14px;color:#333}
</style>
</head>
<body>

<div class="abs topbar">
  <div class="contact email">
    <svg width="15" height="10" viewBox="0 0 15 10"><rect width="15" height="10" fill="#34a6d7"/><path d="M0 0 L7.5 6 L15 0" stroke="#fff" fill="none" stroke-width="1"/></svg>
    info@brightwellhq.example
  </div>
  <div class="contact phone">
    <svg width="9" height="10" viewBox="0 0 9 10"><path d="M1.5 0.5 L3.5 0.5 L4 3 L2.8 4 Q4 6.5 5.5 7.2 L6.5 6 L8.8 6.6 L8.8 8.6 Q6 10.4 2.5 6.5 Q-0.5 3 1.5 0.5Z" fill="#34a6d7"/></svg>
    555-014-2290
  </div>
</div>

<div class="abs brand">
  <div class="dot"></div>
  <div class="name">Brightwell Cleaning Services</div>
</div>

<nav class="abs nav">
  <a class="active" href="#">HOME</a>
  <a href="#">SERVICES</a>
  <a href="#">WHY BRIGHTWELL</a>
  <a href="#">ESTIMATE</a>
  <a href="#">TESTIMONIALS</a>
  <a href="#">CONTACT US</a>
</nav>

<section class="abs hero">
  <div class="ph" role="img" aria-label="Photo of a woman in a grey t-shirt wiping a bright window with a yellow cloth, blue sky and clouds outside"></div>
  <div class="arrow" style="left:20px"><svg width="8" height="10" viewBox="0 0 8 10"><path d="M6 1 L2 5 L6 9" stroke="#333" stroke-width="2" fill="none"/></svg></div>
  <div class="arrow" style="left:729px"><svg width="8" height="10" viewBox="0 0 8 10"><path d="M2 1 L6 5 L2 9" stroke="#333" stroke-width="2" fill="none"/></svg></div>
  <div class="caption">WE ARE RESIDENTIAL, COMMERCIAL CLEANING SERVICE FIRM</div>
</section>

<section class="abs welcome">
  <h1>Welcome To <span>Brightwell Cleaning Services</span></h1>
  <p class="lead"><span class="blue" style="font-weight:400">Brightwell Cleaning Services</span> dolor sit amet, consectetuer adipiscing elit, sed dia</p>
  <p class="body">Lorem ipsum dolor sit amet, consectetuer adipiscing elit, sed diam nonummy nibh euismod tincidunt ut laoreet dolore magna aliquam erat volutpat. Ut wisi enim ad minim veniam, quis nostrud exerci tation ullamcorper suscipit lobortis nisl ut aliquip ex ea commodo consequat. Duis autem vel eum iriure dolor in hendrerit in vulputate velit.</p>
  <a class="btn" href="#">READ MORE</a>
</section>

<aside class="abs inquiry">
  <div class="tab">QUICK INQUIRY</div>
  <div class="field" style="top:26px">First Name <i>*</i></div>
  <div class="field" style="top:53px">Last Name <i>*</i></div>
  <div class="field" style="top:80px">Email <i>*</i></div>
  <div class="field" style="top:107px;height:35px">Address<i>*</i></div>
  <a class="btn" href="#">SUBMIT</a>
</aside>

<h2 class="abs section-title" style="top:688px">Our <span class="blue">Services</span></h2>
<svg class="abs divider" style="top:722px" viewBox="0 0 777 14"><line x1="152" y1="7" x2="360" y2="7" stroke="#ccc"/><line x1="418" y1="7" x2="626" y2="7" stroke="#ccc"/><rect x="383" y="3" width="8" height="8" fill="#34a6d7" transform="rotate(45 387 7)"/></svg>
<p class="abs services-lead">Lorem ipsum dolor sit amet, consectetuer adipiscing elit, sed diam nonummy nibh euismod tincidunt ut</p>

<div class="abs card" style="left:64px">
  <div class="ph" role="img" aria-label="Photo of cleaners in blue overalls washing windows in a home kitchen" style="background:linear-gradient(90deg,#6f9a5a 0%,#e9eef2 25%,#2a4f9e 45%,#d8dde2 60%,#9c6a44 80%,#cfd5da 100%)"></div>
  <div class="label">Residential</div>
</div>
<div class="abs card" style="left:289px">
  <div class="ph" role="img" aria-label="Photo of janitors mopping an office floor beside a yellow caution sign" style="background:linear-gradient(180deg,#c79a6a 0%,#e9dcc8 45%,#efe9df 70%,#e7c64a 100%)"></div>
  <div class="label">Commercial</div>
</div>
<div class="abs card" style="left:516px">
  <div class="ph" role="img" aria-label="Photo of a worker cleaning large glass panels in a building" style="background:linear-gradient(90deg,#3a3f44 0%,#d9dee2 30%,#e67a2e 36%,#eef1f3 50%,#c7ccd0 100%)"></div>
  <div class="label">Extra Services</div>
</div>

<h2 class="abs section-title" style="top:954px">Client <span class="blue">Testimonials</span></h2>
<svg class="abs divider" style="top:988px" viewBox="0 0 777 14"><line x1="135" y1="7" x2="360" y2="7" stroke="#ccc"/><line x1="418" y1="7" x2="608" y2="7" stroke="#ccc"/><rect x="383" y="3" width="8" height="8" fill="#34a6d7" transform="rotate(45 387 7)"/></svg>

<div class="abs testimonial">
  <div class="avatar" role="img" aria-label="Portrait photo of a smiling client giving a thumbs up"></div>
  <div class="quote">&ldquo;</div>
  <p class="words">Lorem ipsum dolor sit amet, consectetuer adipiscing elit, sed diam nonummy nibh euismod tincidunt ut laoreet dolore magna aliq erat volutpat. Ut wisi enim ad minim veniam, quis nostrud exerci tation ullamcorper suscipit lobortis nisl ut aliquip commodoerew consequat. Duis autem vel eum iriure dolor in hendrerit in vulputate velit esse molestie consequat</p>
  <p class="who">Dana Whitfield</p>
</div>
<svg class="abs side-arrow" style="left:31px" width="16" height="30" viewBox="0 0 16 30"><path d="M15 1 L1 15 L15 29" stroke="#666" fill="none" stroke-width="1.2"/></svg>
<svg class="abs side-arrow" style="left:723px" width="16" height="30" viewBox="0 0 16 30"><path d="M1 1 L15 15 L1 29" stroke="#666" fill="none" stroke-width="1.2"/></svg>

<footer class="abs footer">
  <div class="links">Home<span>|</span>Services<span>|</span>Why Brightwell<span>|</span>Estimate<span>|</span>Testimonials<span>|</span>Contact Us</div>
  <div class="copy">Copyright &copy; 2016 Brightwell Cleaning Services.<br>All Rights Reserved.</div>
</footer>

</body>
</html>
```